wealth management firm, professional group, new model

we have a logo that works but we need a card, white background using our colors...clean look

our tag line if can be used in

Clarity Today, Wealth Tomorrow

```html
<!DOCTYPE html>
<html lang="en">
<head>
<meta charset="utf-8">
<title>Arvel Wealth Partners – Business Card</title>
<link rel="stylesheet" href="https://fonts.googleapis.com/css2?family=Montserrat:wght@300;400;500;600&display=swap">
<style>
  :root {
    --bg: #8796ab;
    --navy: #1b2550;
    --navy-deep: #141c40;
    --navy-light: #28356b;
    --silver: #c3c9dc;
    --silver-dim: #8e97b8;
    --paper: #fbfbfc;
    --ink: #1b2550;
    --muted: #7b8296;
  }
  * { box-sizing: border-box; margin: 0; padding: 0; }
  html, body {
    width: 1200px; height: 1200px; overflow: hidden;
    background: var(--bg);
    font-family: "Montserrat", sans-serif;
  }
  .canvas {
    width: 1200px; height: 1200px;
    display: flex; flex-direction: column;
    align-items: center; justify-content: center; gap: 56px;
  }
  .card {
    width: 880px; height: 503px;
    border-radius: 6px;
    position: relative;
    box-shadow: 0 18px 40px rgba(20, 28, 64, 0.25);
    overflow: hidden;
  }

  /* Front */
  .card-front {
    background: linear-gradient(135deg, var(--navy-light) 0%, var(--navy) 50%, var(--navy-deep) 100%);
    display: flex; flex-direction: column; align-items: center;
    padding-top: 150px;
  }
  .front-logo {
    color: var(--silver);
    font-weight: 300;
    font-size: 74px;
    letter-spacing: 0.42em;
    margin-right: -0.42em;
  }
  .front-sub {
    color: var(--silver);
    font-weight: 300;
    font-size: 21px;
    letter-spacing: 0.2em;
    margin-top: 6px;
  }
  .front-tagline {
    color: var(--silver-dim);
    font-weight: 400;
    font-size: 19px;
    letter-spacing: 0.1em;
    text-transform: uppercase;
    margin-top: 78px;
  }

  /* Back */
  .card-back {
    background: var(--paper);
    border-bottom: 6px solid var(--navy);
  }
  .back-logo {
    position: absolute; top: 92px; right: 90px;
    color: var(--ink);
    font-weight: 400;
    font-size: 42px;
    letter-spacing: 0.38em;
  }
  .identity { position: absolute; left: 80px; top: 150px; }
  .person-name {
    color: var(--ink);
    font-weight: 600;
    font-size: 40px;
    letter-spacing: -0.01em;
  }
  .person-role {
    color: var(--muted);
    font-weight: 400;
    font-size: 17px;
    letter-spacing: 0.14em;
    margin-top: 6px;
  }
  .contact-list {
    position: absolute; left: 80px; top: 268px;
    list-style: none;
    display: flex; flex-direction: column; gap: 12px;
  }
  .contact-item {
    display: flex; align-items: flex-start; gap: 16px;
    color: var(--ink);
    font-size: 19px; font-weight: 400; line-height: 1.3;
  }
  .contact-icon { width: 22px; height: 22px; flex: none; margin-top: 2px; }
</style>
</head>
<body>
<main class="canvas">

  <section class="card card-front" aria-label="Card front">
    <div class="front-logo">ARVEL</div>
    <div class="front-sub">WEALTH PARTNERS</div>
    <div class="front-tagline">Clarity Today, Wealth Tomorrow</div>
  </section>

  <section class="card card-back" aria-label="Card back">
    <div class="back-logo">ARVEL</div>

    <div class="identity">
      <h1 class="person-name">DANIEL REEVE</h1>
      <p class="person-role">Managing Director</p>
    </div>

    <ul class="contact-list">
      <li class="contact-item">
        <svg class="contact-icon" viewBox="0 0 24 24" aria-hidden="true">
          <circle cx="12" cy="12" r="12" fill="#1b2550"/>
          <path d="M12 5.5a4 4 0 0 0-4 4c0 3 4 8 4 8s4-5 4-8a4 4 0 0 0-4-4z" fill="#fff"/>
          <circle cx="12" cy="9.5" r="1.5" fill="#1b2550"/>
        </svg>
        <span>245 Harbor Lane<br>Boston, MA 02110, United States</span>
      </li>
      <li class="contact-item">
        <svg class="contact-icon" viewBox="0 0 24 24" aria-hidden="true">
          <circle cx="12" cy="12" r="12" fill="#1b2550"/>
          <path d="M8.6 6.5l1.8-.3 1 2.6-1.2 1a7 7 0 0 0 3.5 3.5l1-1.2 2.6 1-.3 1.8c-.2.8-1 1.2-1.8 1A10 10 0 0 1 7.6 8.3c-.2-.8.2-1.6 1-1.8z" fill="#fff"/>
        </svg>
        <span>(555) 014-2290</span>
      </li>
      <li class="contact-item">
        <svg class="contact-icon" viewBox="0 0 24 24" aria-hidden="true">
          <circle cx="12" cy="12" r="12" fill="#1b2550"/>
          <rect x="6.5" y="8" width="11" height="8" rx="1" fill="#fff"/>
          <path d="M6.8 8.5l5.2 4 5.2-4" fill="none" stroke="#1b2550" stroke-width="1.2"/>
        </svg>
        <span>info@arvelwealth.com</span>
      </li>
      <li class="contact-item">
        <svg class="contact-icon" viewBox="0 0 24 24" aria-hidden="true">
          <circle cx="12" cy="12" r="12" fill="#1b2550"/>
          <g fill="none" stroke="#fff" stroke-width="1.2">
            <circle cx="12" cy="12" r="5.5"/>
            <ellipse cx="12" cy="12" rx="2.4" ry="5.5"/>
            <path d="M6.5 12h11"/>
          </g>
        </svg>
        <span>arvelwealth.com</span>
      </li>
    </ul>
  </section>

</main>
</body>
</html>
```